Dog walking/Pet Sitting company needs a brochure to hook high end apartment tenants

We are looking for a brochure design that we can bring to meetings with high-end apartment and hotel management that will explain who we are, what we do, and how we can help their tenants/guests. I would like it to reflect the same look and feel of our website, carried over to printed brochure. Wesbite is www.hollowbrookpawcare.com. I can provide the stock images from the website if needed. A bi-fold brochure is ideal, unless you feel the information would fit better on a tri-fold. My company colors are #5D4664 and #5BA046. I would like a more professional tone to it, rather than fun.

Target Market(s)

Demo Professional Females and Males ages 30-50 with pets

Industry/Entity Type

Pet sitting

Font styles to use
Sans Serif

Colors
6b449b
9bcb3c

Requirements
Must have
• the same look and feel as my website; explain who we are, what we do, how we can help; include services offered; Mention that we service Maple Ridge and surrounding towns. Mention 15 years in business.
Should not have
• do not list pricing on brochure (you can mention pricing is available on the website). No cartoonish feel.

```html
<!DOCTYPE html>
<html lang="en">
<head>
<meta charset="utf-8">
<title>Hollow Brook Paw Care – Brochure Spread</title>
<link href="https://fonts.googleapis.com/css2?family=Montserrat:ital,wght@0,400;0,500;0,600;0,700;0,800;1,800&display=swap" rel="stylesheet">
<style>
  :root{
    --purple:#5d4664;
    --purple-soft:#6f5677;
    --green:#5ba046;
    --ink:#3b3b3b;
    --paper:#ffffff;
    --page-shade:#f4f4f4;
    --backdrop:#e6e6e6;
  }
  *{box-sizing:border-box;margin:0;padding:0}
  html,body{width:1200px;height:833px;overflow:hidden}
  body{background:var(--backdrop);font-family:"Montserrat",Arial,sans-serif;color:var(--ink);position:relative}
  .page{position:absolute;top:20px;width:560px;height:793px;background:var(--paper);overflow:hidden}
  .page--left{left:40px;background:linear-gradient(to right,var(--paper) 92%,var(--page-shade))}
  .page--right{left:600px;background:linear-gradient(to left,var(--paper) 92%,var(--page-shade))}
  .abs{position:absolute}

  .headline{font-weight:800;font-style:italic;font-size:21px;letter-spacing:.5px;color:var(--purple);text-transform:uppercase;white-space:nowrap}
  .headline .accent{color:var(--green)}
  .bone{display:block}
  .lead{font-size:9.5px;line-height:1.45;color:var(--ink)}

  /* left page */
  .mission-block{left:0;top:150px;width:330px;height:260px;background:var(--green);color:#fff;padding:20px 30px 0 40px}
  .mission-block h2{font-weight:500;font-size:18px;margin-bottom:7px;letter-spacing:.3px}
  .mission-block p{font-size:8.6px;line-height:1.45;margin-bottom:14px;width:250px}
  .photo{background:linear-gradient(135deg,#d9cfc5,#a89a8d 55%,#7f8fa6)}
  .hero-photo{left:300px;top:150px;width:260px;height:280px}

  .service-card{top:450px;width:152px}
  .service-card .photo{height:78px}
  .service-card .label{background:var(--green);color:#fff;font-size:10px;font-weight:600;text-align:center;padding:5px 0;text-transform:uppercase;letter-spacing:.5px}
  .service-card .body{background:var(--purple);color:#fff;font-size:7.4px;line-height:1.4;text-align:center;padding:8px 10px 22px}
  .service-card .pill{display:block;margin:-11px auto 0;width:86px;background:var(--green);color:#fff;font-size:8px;font-weight:700;text-align:center;border-radius:10px;padding:5px 0;position:relative}

  /* right page */
  .review{left:40px;width:490px;height:58px}
  .review .photo{position:absolute;left:0;top:0;width:100px;height:58px;background:linear-gradient(135deg,#8a7a66,#3d3a36)}
  .review .quote{position:absolute;left:100px;top:0;right:0;height:58px;color:#fff;font-size:9px;line-height:1.4;padding:9px 26px 0 30px}
  .review .quote::before{content:"\201C";position:absolute;left:10px;top:2px;font-size:22px;opacity:.6}
  .review .quote::after{content:"\201D";position:absolute;right:8px;bottom:-8px;font-size:22px;opacity:.6}
  .quote--green{background:var(--green)}
  .quote--purple{background:var(--purple-soft)}

  .steps{left:30px;top:490px;width:510px;display:flex;justify-content:space-between}
  .step{width:118px;text-align:center}
  .step .icon{width:48px;height:48px;border:1.5px solid var(--green);border-radius:50%;margin:0 auto 8px;display:flex;align-items:center;justify-content:center}
  .step h3{font-size:10px;font-weight:700;color:var(--purple);line-height:1.2;min-height:25px}
  .step .bone{margin:3px auto 6px}
  .step p{font-size:7.4px;line-height:1.45;color:var(--ink)}
</style>
</head>
<body>

<section class="page page--left">
  <h1 class="headline abs" style="left:40px;top:38px">Life is a <span class="accent">balancing act.</span></h1>
  <svg class="bone abs" style="left:40px;top:66px" width="22" height="8" viewBox="0 0 22 8"><rect x="4" y="3" width="14" height="2" fill="#5ba046"/><circle cx="3" cy="2" r="2" fill="#5ba046"/><circle cx="3" cy="6" r="2" fill="#5ba046"/><circle cx="19" cy="2" r="2" fill="#5ba046"/><circle cx="19" cy="6" r="2" fill="#5ba046"/></svg>
  <p class="lead abs" style="left:40px;top:82px;width:480px">With Hollow Brook Paw Care, you will be able to focus on your life without sacrificing the needs of your pets. We offer a complimentary consultation and an online client portal/app to ensure that your pet's information is always up-to-date and scheduling is hassle-free. Let us afford you the luxury of time—life's greatest commodity—so you can effortlessly navigate life's to-do list.</p>

  <div class="mission-block abs">
    <h2>We're on a Mission</h2>
    <p>We promise to improve your pet's quality of life by consistently providing the highest level of pet care. We are dedicated to providing your pets a safe, comfortable and caring experience. We promise to keep your pet happy and healthy while providing you peace of mind.</p>
    <h2>Support Local</h2>
    <p>We are a small business that has served the Maple Ridge community for close to 15 years! We give back to our community by helping local charitable organizations. We support the local economy by hiring employees and networking with other small businesses to build meaningful relationships.</p>
  </div>
  <div class="photo hero-photo abs" role="img" aria-label="Photo of a relaxed tabby cat held in its owner's arms"></div>

  <article class="service-card abs" style="left:30px">
    <div class="photo" role="img" aria-label="Photo of a dog holding its leash"></div>
    <div class="label">Dog Walking</div>
    <div class="body">Mid-day dog walks keep your stay-at-home pup entertained while you attend to work or a day of play!</div>
    <span class="pill">I WORK!</span>
  </article>
  <article class="service-card abs" style="left:204px">
    <div class="photo" role="img" aria-label="Photo of a small dog sitting in a suitcase"></div>
    <div class="label">Boarding</div>
    <div class="body">Leave your dogs with us and your guilt at the door. Devote your attention to your travels while we love on your pups!</div>
    <span class="pill">I TRAVEL!</span>
  </article>
  <article class="service-card abs" style="left:378px">
    <div class="photo" role="img" aria-label="Photo of a pet owner relaxing at home with her dog"></div>
    <div class="label">Pet Sitting</div>
    <div class="body">Pet care services in your home allow you to focus on fun knowing that your pets are being well-cared for.</div>
    <span class="pill">I'M ACTIVE!</span>
  </article>
</section>

<section class="page page--right">
  <h1 class="headline abs" style="left:40px;top:38px">Here's what our <span class="accent">clients say.</span></h1>
  <svg class="bone abs" style="left:40px;top:66px" width="22" height="8" viewBox="0 0 22 8"><rect x="4" y="3" width="14" height="2" fill="#5ba046"/><circle cx="3" cy="2" r="2" fill="#5ba046"/><circle cx="3" cy="6" r="2" fill="#5ba046"/><circle cx="19" cy="2" r="2" fill="#5ba046"/><circle cx="19" cy="6" r="2" fill="#5ba046"/></svg>
  <p class="lead abs" style="left:40px;top:82px;width:480px">We love our Clients! Our Clients love us back! We strive to maintain our impeccable reputation; check out our reviews on Searchly and Localrate and feel the love!</p>

  <div class="review abs" style="top:120px">
    <div class="photo" role="img" aria-label="Photo of a happy black and white dog"></div>
    <p class="quote quote--green">You all not only take such great care of our most precious family member, you take such great care of us too by giving us such enjoyment and comfort from these daily reports and photos!</p>
  </div>
  <div class="review abs" style="top:182px">
    <div class="photo" role="img" aria-label="Photo of a spotted dog sitting on pavement"></div>
    <p class="quote quote--purple">I can't believe that I am lucky enough to have someone I trust on this level with my dog. There aren't enough words to recommend this business as much as I'd like to.</p>
  </div>
  <div class="review abs" style="top:244px">
    <div class="photo" role="img" aria-label="Photo of a fluffy tan puppy"></div>
    <p class="quote quote--green">I schedule my travel and vacation around their availability. I will not let anyone else watch my crazy 4-legged baby!</p>
  </div>
  <div class="review abs" style="top:306px">
    <div class="photo" role="img" aria-label="Photo of a golden retriever"></div>
    <p class="quote quote--purple">Hands down the best! Extremely friendly, reliable, and professional...flexible and easy to work with around crazy schedules.</p>
  </div>

  <h1 class="headline abs" style="left:40px;top:392px">Ready to free up <span class="accent">your time?</span></h1>
  <p class="lead abs" style="left:40px;top:424px;width:480px">We are here to uncomplicate your life! Our systems and processes allow for seamless scheduling, service and billing. Give us a few minutes of your time and we will deliver it back to you tenfold!</p>

  <div class="steps abs">
    <div class="step">
      <div class="icon"><svg width="26" height="22" viewBox="0 0 26 22"><rect x="1" y="1" width="24" height="15" rx="1.5" fill="none" stroke="#5d4664" stroke-width="1.6"/><rect x="4" y="4" width="18" height="9" fill="#5ba046"/><path d="M9 21h8M13 16v5" stroke="#5d4664" stroke-width="1.6"/></svg></div>
      <h3>Online Registration</h3>
      <svg class="bone" width="16" height="6" viewBox="0 0 22 8"><rect x="4" y="3" width="14" height="2" fill="#5ba046"/><circle cx="3" cy="2" r="2" fill="#5ba046"/><circle cx="3" cy="6" r="2" fill="#5ba046"/><circle cx="19" cy="2" r="2" fill="#5ba046"/><circle cx="19" cy="6" r="2" fill="#5ba046"/></svg>
      <p>Click on the register link on our homepage to begin online registration or submit a request form if you would like more information first.</p>
    </div>
    <div class="step">
      <div class="icon"><svg width="26" height="22" viewBox="0 0 26 22"><path d="M3 2h20a2 2 0 0 1 2 2v10a2 2 0 0 1-2 2H10l-5 5v-5H3a2 2 0 0 1-2-2V4a2 2 0 0 1 2-2z" fill="#5ba046"/><circle cx="8" cy="9" r="1.4" fill="#fff"/><circle cx="13" cy="9" r="1.4" fill="#fff"/><circle cx="18" cy="9" r="1.4" fill="#fff"/></svg></div>
      <h3>Complimentary Consultation</h3>
      <svg class="bone" width="16" height="6" viewBox="0 0 22 8"><rect x="4" y="3" width="14" height="2" fill="#5ba046"/><circle cx="3" cy="2" r="2" fill="#5ba046"/><circle cx="3" cy="6" r="2" fill="#5ba046"/><circle cx="19" cy="2" r="2" fill="#5ba046"/><circle cx="19" cy="6" r="2" fill="#5ba046"/></svg>
      <p>Request a consultation through our online portal. Get stuck? Then we'll reach out to you if you coordinate a meeting at your convenience.</p>
    </div>
    <div class="step">
      <div class="icon"><svg width="24" height="24" viewBox="0 0 24 24"><rect x="1" y="3" width="22" height="20" rx="1.5" fill="none" stroke="#5d4664" stroke-width="1.6"/><rect x="1" y="3" width="22" height="5" fill="#5ba046"/><g fill="#5ba046"><rect x="4" y="11" width="3" height="3"/><rect x="10" y="11" width="3" height="3"/><rect x="16" y="11" width="3" height="3"/><rect x="4" y="17" width="3" height="3"/><rect x="10" y="17" width="3" height="3"/></g></svg></div>
      <h3>Flexible Scheduling</h3>
      <svg class="bone" width="16" height="6" viewBox="0 0 22 8"><rect x="4" y="3" width="14" height="2" fill="#5ba046"/><circle cx="3" cy="2" r="2" fill="#5ba046"/><circle cx="3" cy="6" r="2" fill="#5ba046"/><circle cx="19" cy="2" r="2" fill="#5ba046"/><circle cx="19" cy="6" r="2" fill="#5ba046"/></svg>
      <p>Once we've met, we will be able to custom schedule your visits to fit your needs. You can always adjust your schedule through our portal app if your needs change.</p>
    </div>
    <div class="step">
      <div class="icon"><svg width="26" height="20" viewBox="0 0 26 20"><path d="M2 5h6l2-3h6l2 3h6v14H2z" fill="#5d4664"/><circle cx="13" cy="11" r="5" fill="#fff"/><circle cx="13" cy="11" r="3" fill="#5ba046"/></svg></div>
      <h3>Visits with Reports and Photos</h3>
      <svg class="bone" width="16" height="6" viewBox="0 0 22 8"><rect x="4" y="3" width="14" height="2" fill="#5ba046"/><circle cx="3" cy="2" r="2" fill="#5ba046"/><circle cx="3" cy="6" r="2" fill="#5ba046"/><circle cx="19" cy="2" r="2" fill="#5ba046"/><circle cx="19" cy="6" r="2" fill="#5ba046"/></svg>
      <p>Your pets will be cared for by our elite team of Pet Care Specialists. After each visit, you will receive an emailed report with photo.</p>
    </div>
  </div>
</section>

</body>
</html>
```